4' x 8' Construction Project Sign, think of a very large business card

We need project signs for our construction sites, the sign will be mounted along the road so cars driving by can quickly read. the sign should be able to be read as cars drive by doing highway speed.

Think like your making a large business card

I would like to include "NOW HIRING" Superintendents, Project Managers, Pipe Foremen, Pipe Layers, and Equipment Operators

Description of services we provide should include

Civil Construction Services
Land Clearing
Excavation
Underground Utilities
Environmental Maintenance

The 2 objectives is to market to future clients and to recruit new employees

The sign will be mounted on posts at the entrance of our construction projects
Updates

Low design quality

Target Market(s)

Construction and land developers

Industry/Entity Type

Construction Company

Other font styles liked:
• Hypatia Sans Pro lite

Colors

Designer to choose colors to be used in the design.

Requirements
Must have
• Clean and easy to read
• Civil Construction Services
• Land Clearing
• Excavation
• Underground Utilities
• Road Construction

```html
<!DOCTYPE html>
<html lang="en">
<head>
<meta charset="utf-8">
<title>Harlow Brothers – Now Hiring Project Sign</title>
<link rel="stylesheet" href="https://fonts.googleapis.com/css2?family=Open+Sans:wght@700;800&family=Montserrat:wght@400;600&display=swap">
<style>
  :root {
    --navy: #223f7c;
    --slate: #606162;
    --white: #ffffff;
    --backdrop: #e6e7e9;
  }
  html, body {
    margin: 0;
    padding: 0;
    width: 1200px;
    height: 701px;
    overflow: hidden;
    background: var(--backdrop);
  }
  .sign {
    position: absolute;
    left: 50px;
    top: 75px;
    width: 1100px;
    height: 550px;
    overflow: hidden;
    background: var(--slate);
  }
  .sign__shapes {
    position: absolute;
    inset: 0;
  }
  .headline {
    position: absolute;
    left: 54px;
    margin: 0;
    font-family: "Open Sans", sans-serif;
    font-weight: 800;
    font-size: 140px;
    line-height: 1;
    color: var(--white);
    letter-spacing: -1px;
  }
  .headline--now { top: 31px; }
  .headline--hiring { top: 160px; }

  .positions {
    position: absolute;
    left: 633px;
    top: 46px;
    margin: 0;
    padding: 0;
    list-style: none;
  }
  .positions__item {
    display: flex;
    align-items: center;
    height: 49px;
    font-family: "Open Sans", sans-serif;
    font-weight: 700;
    font-size: 32px;
    color: var(--white);
  }
  .positions__tick {
    width: 30px;
    height: 30px;
    margin-right: 19px;
    flex: none;
  }

  .services {
    position: absolute;
    left: 62px;
    top: 340px;
    margin: 0;
    padding: 0;
    list-style: none;
  }
  .services__item {
    display: flex;
    align-items: center;
    height: 38px;
    margin-bottom: 0;
    font-family: "Montserrat", sans-serif;
    font-weight: 400;
    font-size: 23px;
    color: var(--white);
  }
  .services__item:nth-child(2) { margin-bottom: 3px; }
  .services__item:nth-child(4) { margin-bottom: 3px; }
  .services__bullet {
    width: 15px;
    height: 15px;
    margin-right: 15px;
    border: 2px solid var(--white);
    box-sizing: border-box;
    flex: none;
  }

  .brand {
    position: absolute;
    left: 644px;
    top: 393px;
    display: flex;
    align-items: center;
    gap: 18px;
  }
  .brand__square {
    width: 64px;
    height: 64px;
    background: var(--navy);
    flex: none;
  }
  .brand__name {
    font-family: "Montserrat", sans-serif;
    font-weight: 600;
    font-size: 30px;
    line-height: 1.15;
    color: var(--navy);
    text-transform: uppercase;
    letter-spacing: 0.5px;
  }
</style>
</head>
<body>
  <main class="sign">
    <svg class="sign__shapes" width="1100" height="550" viewBox="0 0 1100 550" aria-hidden="true">
      <rect class="band band--top" x="0" y="0" width="1100" height="321" fill="var(--navy)"/>
      <polygon class="panel panel--brand" points="596,321 1100,321 1100,550 568,550 525,462" fill="var(--white)"/>
      <polygon class="accent-wedge" points="525,462 483,550 568,550" fill="var(--navy)"/>
    </svg>

    <h1 class="headline headline--now">NOW</h1>
    <h1 class="headline headline--hiring">HIRING</h1>

    <ul class="positions">
      <li class="positions__item"><svg class="positions__tick" viewBox="0 0 30 30"><path d="M24 8 A12 12 0 1 0 27 15" fill="none" stroke="#fff" stroke-width="2"/><path d="M8 14 L14 21 L27 5" fill="none" stroke="#fff" stroke-width="2.6" stroke-linecap="round" stroke-linejoin="round"/></svg>Superintendents</li>
      <li class="positions__item"><svg class="positions__tick" viewBox="0 0 30 30"><path d="M24 8 A12 12 0 1 0 27 15" fill="none" stroke="#fff" stroke-width="2"/><path d="M8 14 L14 21 L27 5" fill="none" stroke="#fff" stroke-width="2.6" stroke-linecap="round" stroke-linejoin="round"/></svg>Project Managers</li>
      <li class="positions__item"><svg class="positions__tick" viewBox="0 0 30 30"><path d="M24 8 A12 12 0 1 0 27 15" fill="none" stroke="#fff" stroke-width="2"/><path d="M8 14 L14 21 L27 5" fill="none" stroke="#fff" stroke-width="2.6" stroke-linecap="round" stroke-linejoin="round"/></svg>Pipe Foremen</li>
      <li class="positions__item"><svg class="positions__tick" viewBox="0 0 30 30"><path d="M24 8 A12 12 0 1 0 27 15" fill="none" stroke="#fff" stroke-width="2"/><path d="M8 14 L14 21 L27 5" fill="none" stroke="#fff" stroke-width="2.6" stroke-linecap="round" stroke-linejoin="round"/></svg>Pipe Layers</li>
      <li class="positions__item"><svg class="positions__tick" viewBox="0 0 30 30"><path d="M24 8 A12 12 0 1 0 27 15" fill="none" stroke="#fff" stroke-width="2"/><path d="M8 14 L14 21 L27 5" fill="none" stroke="#fff" stroke-width="2.6" stroke-linecap="round" stroke-linejoin="round"/></svg>Equipment Operators</li>
    </ul>

    <ul class="services">
      <li class="services__item"><span class="services__bullet"></span>Civil Construction Services</li>
      <li class="services__item"><span class="services__bullet"></span>Land Clearing</li>
      <li class="services__item"><span class="services__bullet"></span>Excavation</li>
      <li class="services__item"><span class="services__bullet"></span>Underground Utilities</li>
      <li class="services__item"><span class="services__bullet"></span>Environmental Maintenance</li>
    </ul>

    <div class="brand">
      <span class="brand__square"></span>
      <span class="brand__name">Harlow Brothers<br>Civil Construction</span>
    </div>
  </main>
</body>
</html>
```